wooden jewelry - pearl necklaces

I sell wooden jeweler (rings and pearls) on markets, and so on. I also opened my business as a carpenter. The rings and a combination of wood and metal. The wood is special wood, not very common on Europe. I paint the rings afterwards. You can see some of the pictures on the pictures I uploaded. The pearls are made of the same kind of wood and colored in all kinds of colors. They are then assembled to bracelets. The jewelry is very individual and looks really cool and all kinds of people.

Target Market(s)

Young urban alternative with a sense of individuality

Contact Information for Business Card

Front:

Text:

„Kugelwerk“ (big)
„Malte Oswitz“ (smaler)

Back
„Holzschmuck
Herstellung von individuellem Holz- und Modeschmuck

Malte Oswitz
Tel: 015239460518
Lindgarbweg 9
83127 Kieselbach

malteoswitz@postfeld.de“

Font styles to use
Sans Serif

Requirements
Nice to have
• Nice to see a camel thorn tree on the background, this is a special wood and some of the rings are made out of this wood.

```html
<!DOCTYPE html>
<html lang="de">
<head>
<meta charset="utf-8">
<title>Kugelwerk – Visitenkarte</title>
<link rel="stylesheet" href="https://fonts.googleapis.com/css2?family=Jost:wght@500;600;700&family=Open+Sans:wght@400;500&display=swap">
<style>
  :root {
    --page: #ffffff;
    --wood-light: #8a7b6e;
    --wood-dark: #5c4f47;
    --ring-red: #6d2a3a;
    --band-white: #f4f5f7;
    --panel-dark: #3a312d;
    --beads-dark: #1e191d;
    --beads-mid: #3b2e2e;
    --text-light: #ffffff;
  }
  * { margin: 0; padding: 0; box-sizing: border-box; }
  html, body {
    width: 1200px; height: 900px; overflow: hidden;
    background: var(--page);
  }
  .canvas { position: relative; width: 1200px; height: 900px; }

  .card {
    position: absolute;
    left: 286px;
    width: 574px;
    height: 327px;
    border-radius: 14px;
    overflow: hidden;
    color: var(--text-light);
  }
  .card--back { top: 88px; }
  .card--front { top: 498px; }

  /* back side */
  .back-photo {
    position: absolute; inset: 0 0 auto 0; height: 200px;
    background:
      radial-gradient(ellipse 120px 90px at 300px 60px, rgba(109,42,58,.75), transparent 70%),
      radial-gradient(ellipse 80px 70px at 250px 70px, rgba(150,170,200,.55), transparent 70%),
      linear-gradient(135deg, var(--wood-light), var(--wood-dark));
  }
  .back-panel {
    position: absolute; inset: 0;
  }
  .brand {
    position: absolute; left: 30px; top: 36px;
    font-family: "Jost", sans-serif; font-weight: 500;
    font-size: 29px; letter-spacing: 0.04em; line-height: 1;
  }
  .brand__tagline {
    display: block; margin-top: 6px;
    font-family: "Open Sans", sans-serif; font-weight: 500;
    font-size: 5.2px; letter-spacing: 0.06em;
  }
  .owner {
    position: absolute; right: 29px; top: 40px;
    font-family: "Jost", sans-serif; font-weight: 500;
    font-size: 23px; letter-spacing: 0.04em; line-height: 1;
  }
  .contact {
    position: absolute; top: 202px;
    font-family: "Open Sans", sans-serif; font-size: 13.5px; line-height: 20px;
    text-align: center;
  }
  .contact svg { display: block; margin: 0 auto 14px; }
  .contact--phone { left: 30px; text-align: left; }
  .contact--phone svg { margin-left: 38px; }
  .contact--mail { left: 200px; width: 160px; }
  .contact--place { left: 416px; width: 140px; }

  /* front side */
  .front-photo {
    position: absolute; inset: 0;
    background:
      radial-gradient(circle 60px at 80px 60px, rgba(120,90,70,.35), transparent 70%),
      radial-gradient(circle 70px at 480px 260px, rgba(110,80,60,.3), transparent 70%),
      radial-gradient(circle 50px at 300px 40px, rgba(90,40,50,.3), transparent 70%),
      linear-gradient(160deg, var(--beads-mid), var(--beads-dark) 60%);
  }
  .front-name {
    position: absolute; left: 0; right: 0; top: 98px; text-align: center;
    font-family: "Jost", sans-serif; font-weight: 600;
    font-size: 78px; line-height: 1; letter-spacing: 0.01em;
  }
  .front-owner {
    position: absolute; left: 0; right: 0; top: 196px; text-align: center;
    font-family: "Open Sans", sans-serif; font-weight: 400;
    font-size: 33px; line-height: 1; letter-spacing: 0.42em;
    padding-left: 0.42em;
  }
</style>
</head>
<body>
<main class="canvas">

  <section class="card card--back" aria-label="Rückseite">
    <div class="back-photo" role="img" aria-label="Foto eines lackierten Holzrings mit Metallkern auf einer Holzscheibe"></div>
    <svg class="back-panel" width="574" height="327" viewBox="0 0 574 327" aria-hidden="true">
      <polygon points="0,196 336,196 371,162 402,128 574,128 574,327 0,327" fill="var(--panel-dark)"/>
      <polygon points="0,162 371,162 336,196 0,196" fill="var(--band-white)"/>
      <polygon points="432,128 574,128 574,160 400,160" fill="var(--band-white)"/>
    </svg>

    <div class="brand">HOLZSCHMUCK
      <span class="brand__tagline">HERSTELLUNG VON INDIVIDUELLEM HOLZ- UND MODESCHMUCK</span>
    </div>
    <div class="owner">MALTE OSWITZ</div>

    <div class="contact contact--phone">
      <svg width="14" height="16" viewBox="0 0 24 24" aria-hidden="true"><path fill="#fff" d="M6.6 2.5c.6-.4 1.4-.2 1.8.4l2.2 3.5c.4.6.2 1.4-.3 1.8l-1.6 1.2c.9 2.2 2.6 4.3 4.7 5.6l1.4-1.5c.5-.5 1.3-.6 1.8-.2l3.3 2.4c.6.4.7 1.2.3 1.8l-1.4 2c-.8 1.1-2.3 1.6-3.6 1-5.2-2.3-9-6.8-10.7-12.2-.4-1.3.1-2.8 1.3-3.6z"/></svg>
      015239460518
    </div>
    <div class="contact contact--mail">
      <svg width="22" height="16" viewBox="0 0 22 16" aria-hidden="true"><rect x="1" y="1" width="20" height="14" fill="#fff"/><path d="M1 1l10 8 10-8" fill="none" stroke="var(--panel-dark)" stroke-width="1.4"/></svg>
      malteoswitz@postfeld.de
    </div>
    <div class="contact contact--place">
      <svg width="18" height="20" viewBox="0 0 18 20" aria-hidden="true"><path d="M9 1a6 6 0 0 0-6 6c0 4 6 9 6 9s6-5 6-9a6 6 0 0 0-6-6z" fill="none" stroke="#fff" stroke-width="1.6"/><circle cx="9" cy="7" r="2" fill="#fff"/><path d="M2 19h14" stroke="#fff" stroke-width="1.6"/></svg>
      Lindgarbweg 9<br>83127 Kieselbach
    </div>
  </section>

  <section class="card card--front" aria-label="Vorderseite">
    <div class="front-photo" role="img" aria-label="Abgedunkeltes Foto vieler bunter Holzperlen"></div>
    <h1 class="front-name">Kugelwerk</h1>
    <p class="front-owner">Malte Oswitz</p>
  </section>

</main>
</body>
</html>
```